Ridgeford Masonry- Business Card Design

We need a business card design for a new company based in Canberra ACT. We build Rock Retaining Walls, commercial and domestic.
We would like to see designs that use RM letters combine as logo and use stone sandstone or blue rocks. Final design of the business card should communicate strong, wealthy, Rock retaining walls

Target Market(s)

Everybody who needs stone retaining wall in there backyard

Industry/Entity Type

Business

Contact Information for Business Card

RM
Ridgeford Masonry,
Tobin Haraldsen (Stonemason)
Phone/ 0498 315 287
PO Box 3958 Kelvale ACT 2615
E-mail/tharaldsen@oakmail.net.au
www.ridgefordmasonry.com.au

Requirements
Must have
• Letters RM combine as logo. "RIDGEFORD MASONRY" as features
Nice to have
• Rock: Sandstone or bluestone

```html
<!DOCTYPE html>
<html lang="en">
<head>
<meta charset="utf-8">
<title>Ridgeford Masonry – Business Card</title>
<link rel="stylesheet" href="https://fonts.googleapis.com/css2?family=Archivo+Black&family=Questrial&display=swap">
<style>
  :root {
    --sandstone-light: #c9b89a;
    --sandstone-mid: #a88a60;
    --sandstone-dark: #6e5536;
    --shadow-brown: #2a1a0c;
    --band-brown: #5a3210;
    --band-edge: #3a1e08;
    --title-gold: #c98a3c;
    --logo-brown: #3b200c;
    --text-white: #ffffff;
    --text-dark: #2b1a0c;
  }
  * { margin: 0; padding: 0; box-sizing: border-box; }
  html, body {
    width: 1200px; height: 741px; overflow: hidden;
    background: #ffffff;
  }
  .card {
    position: relative;
    width: 1200px; height: 741px;
    overflow: hidden;
    font-family: "Questrial", "Century Gothic", sans-serif;
  }
  .stone-wall {
    position: absolute; inset: 0;
    background:
      linear-gradient(172deg, rgba(30,18,8,0.92) 0%, rgba(40,24,10,0.75) 11%, rgba(0,0,0,0) 19%),
      linear-gradient(90deg, rgba(60,40,20,0.35) 0%, rgba(0,0,0,0) 30%, rgba(0,0,0,0) 70%, rgba(40,25,10,0.35) 100%),
      radial-gradient(ellipse at 55% 55%, var(--sandstone-light) 0%, var(--sandstone-mid) 60%, var(--sandstone-dark) 100%);
  }
  .accent-band {
    position: absolute; left: 0; width: 1200px;
    top: 540px; height: 34px;
    background: rgba(90, 50, 16, 0.85);
    border-top: 3px solid var(--band-edge);
    border-bottom: 2px solid var(--band-edge);
  }
  .brand-title {
    position: absolute; right: 52px; top: 92px;
    font-family: "Archivo Black", "Arial Black", sans-serif;
    font-size: 60px; line-height: 64px;
    letter-spacing: 3px;
    color: var(--title-gold);
    text-align: right;
  }
  .logo {
    position: absolute; left: 62px; top: 220px;
    display: flex; align-items: center; gap: 22px;
  }
  .logo-mark {
    width: 120px; height: 120px;
    background: var(--logo-brown);
  }
  .logo-name {
    font-family: "Archivo Black", "Arial Black", sans-serif;
    font-size: 40px; line-height: 46px;
    color: var(--logo-brown);
    letter-spacing: 2px;
  }
  .contact {
    position: absolute; right: 27px; top: 362px;
    text-align: right; color: var(--text-white);
  }
  .contact .name { font-size: 40px; line-height: 42px; letter-spacing: 1px; }
  .contact .role { font-size: 17px; line-height: 20px; color: var(--text-dark); }
  .contact .phone { font-size: 44px; line-height: 46px; margin-top: 2px; }
  .contact .line { font-size: 20px; line-height: 24px; letter-spacing: 0.5px; }
  .contact .web { font-size: 22px; line-height: 28px; margin-top: 1px; letter-spacing: 0.5px; }
</style>
</head>
<body>
  <div class="card">
    <div class="stone-wall" role="img" aria-label="Photograph of a sandstone crazy-paving rock wall with a dark shadow across the top"></div>
    <div class="accent-band"></div>

    <h1 class="brand-title">RIDGEFORD<br>MASONRY</h1>

    <div class="logo">
      <div class="logo-mark"></div>
      <div class="logo-name">RIDGEFORD<br>MASONRY</div>
    </div>

    <div class="contact">
      <p class="name">TOBIN HARALDSEN</p>
      <p class="role">(STONEMASON)</p>
      <p class="phone">PHONE/ 0498 315 287</p>
      <p class="line">PO BOX 3958 KELVALE ACT 2615</p>
      <p class="line">E-MAIL/THARALDSEN@OAKMAIL.NET.AU</p>
      <p class="web">WWW.RIDGEFORDMASONRY.COM.AU</p>
    </div>
  </div>
</body>
</html>
```